Vantrisco website redesign

1.logo redesign
2. whole website lay out redesign
3. add more function and pages (have some detail in attachment).
4. design the info taking form layout(contact us, return request, trade pro, see all form in file)
5. also design the mobile look for the website
some reference website: https://www.plaquevora.example/
https://www.moskuden.example/

we want our website style between these two website, website should be user friendly focus + slight design style, and mobile one could more like https://www.moskuden.example/ (more design style)

Target Market(s)

Tile Ecommerce

Industry/Entity Type

Ecommerce, Tile

Coding

Coded - Design and coding required

Number of Pages Required

5+ page

```html
<!DOCTYPE html>
<html lang="en">
<head>
<meta charset="utf-8">
<title>Vantrisco — Italian Porcelain Tile</title>
<link href="https://fonts.googleapis.com/css2?family=Cormorant+Garamond:wght@500;600&family=DM+Sans:wght@400;500&display=swap" rel="stylesheet">
<style>
:root{
  --ink:#111114;
  --muted:#55555c;
  --line:#d9d9dd;
  --dark:#1d1c24;
  --white:#ffffff;
  --star:#f3a533;
  --serif:"Cormorant Garamond", Georgia, serif;
  --sans:"DM Sans", Arial, sans-serif;
}
*{box-sizing:border-box;margin:0;padding:0}
html,body{width:1200px;height:3676px;overflow:hidden}
body{position:relative;background:var(--white);color:var(--ink);font-family:var(--sans)}
.abs{position:absolute}
.serif{font-family:var(--serif);font-weight:500}
.fill{display:block}

.topbar{left:0;top:0;width:1200px;height:30px;background:var(--dark);color:#fff;font-size:12px;letter-spacing:3px;text-align:center;line-height:30px}

.brand{display:flex;align-items:center;gap:10px;font-family:var(--serif);font-weight:600;font-size:40px;color:var(--ink)}
.brand .mark{width:30px;height:30px;background:var(--ink)}
.brand.light{color:#fff}
.brand.light .mark{background:#fff}

.search{left:447px;top:55px;width:306px;height:44px;border:1px solid var(--line);font-size:12px;color:var(--muted);padding:0 20px;line-height:42px}
.search svg{position:absolute;right:14px;top:11px}
.icons{left:834px;top:58px;display:flex;gap:22px;align-items:center}
.social-sq{width:30px;height:30px;border-radius:6px}

.nav{left:117px;top:126px;width:965px;height:62px;border-top:1px solid var(--line);border-bottom:1px solid var(--line);display:flex;justify-content:space-between;align-items:center;font-size:12px;color:var(--muted)}

.hero-title{left:117px;top:262px;font-size:64px;line-height:66px}
.hero-text{left:117px;top:420px;width:440px;font-size:14px;line-height:24px;color:var(--muted)}
.btn{display:flex;align-items:center;justify-content:center;gap:8px;font-size:12px;border:1px solid var(--ink);color:var(--ink)}
.btn.dark-outline{border-color:#fff;color:#fff}
.btn.solid{background:#fff;border-color:#fff;color:var(--ink)}

.section-title{left:0;width:1200px;text-align:center;font-size:44px}
.journey-card{top:748px;width:225px;height:208px}
.journey-label{top:976px;width:225px;text-align:center;font-size:14px;font-weight:500}

.dark{left:0;top:1046px;width:1200px;height:664px;background:var(--dark);color:#fff}
.coll-img{top:128px;width:307px;height:292px}
.coll-title{top:442px;width:307px;text-align:center;font-size:15px;font-weight:500}
.coll-text{top:470px;width:307px;text-align:center;font-size:11.5px;line-height:17px;color:#e6e6ea}

.swatch{top:1828px;width:239px;height:230px}
.color-label{top:2074px;width:239px;text-align:center;font-size:14px;font-weight:500}
.dots{top:2101px;width:239px;display:flex;justify-content:center;gap:9px}
.dots span{width:15px;height:15px;border-radius:50%}

.gallery{top:2390px;width:298px;height:263px}
.cart-pin{width:44px;height:44px;border-radius:50%;background:#fff;border:3px solid #d7d7da;display:flex;align-items:center;justify-content:center}
.cart-pin.on{background:var(--ink);border-color:#fff}

.review{top:2878px;width:307px;height:300px;border:1px solid var(--line);border-radius:22px;background:#fff;padding:48px 30px 0 32px}
.review.focus{background:#f6f6f7;box-shadow:0 10px 24px rgba(0,0,0,.12)}
.quote{font-family:var(--serif);font-weight:600;font-size:56px;line-height:40px;height:40px}
.quote.badge{width:56px;height:56px;border-radius:50%;background:var(--ink);color:#fff;text-align:center;line-height:72px;margin-top:-18px;margin-bottom:2px}
.stars{color:var(--star);font-size:17px;letter-spacing:5px;margin-top:12px}
.review p{font-size:11.5px;line-height:22px;color:var(--muted);margin-top:8px}
.review .name{font-family:var(--serif);font-weight:600;font-size:15px;color:var(--ink);margin-top:10px}
.review .role{font-size:12px;color:var(--muted)}

.footer{left:0;top:3286px;width:1200px;height:390px;background:var(--dark);color:#fff}
.f-head{font-family:var(--serif);font-weight:500;font-size:17px}
.f-list{list-style:none;font-size:11.5px;line-height:28.6px}
.f-list li::before{content:"•";margin-right:6px}
.f-contact{display:flex;align-items:center;gap:14px;font-size:12px}
.f-contact .ic{width:30px;height:30px;border:1px solid #fff;display:flex;align-items:center;justify-content:center}
.pay{width:46px;height:28px;border-radius:3px;background:#fff;color:var(--ink);font-size:8.5px;font-weight:500;display:flex;align-items:center;justify-content:center}
</style>
</head>
<body>

<div class="abs topbar">5 SAMPLES FOR $5 (FREE SHIPPING). DETAILS</div>

<header>
  <div class="abs brand" style="left:117px;top:55px"><span class="mark"></span>Vantrisco</div>
  <div class="abs search">Search tile collection
    <svg width="20" height="20" viewBox="0 0 20 20" fill="none" stroke="#111" stroke-width="1.8"><circle cx="8.5" cy="8.5" r="6.5"/><path d="M13.5 13.5l5 5"/></svg>
  </div>
  <div class="abs icons">
    <svg width="22" height="22" viewBox="0 0 22 22" fill="none" stroke="#111" stroke-width="1.6"><circle cx="11" cy="7" r="4.5"/><path d="M3 21c0-5 3.5-8 8-8s8 3 8 8"/></svg>
    <span style="width:38px;height:38px;border-radius:50%;background:var(--ink);display:flex;align-items:center;justify-content:center">
      <svg width="18" height="18" viewBox="0 0 18 18" fill="#fff"><path d="M1 2h3l2 9h9l2-6H5" stroke="#fff" stroke-width="1.5" fill="none"/><circle cx="7" cy="15" r="1.5"/><circle cx="14" cy="15" r="1.5"/></svg>
    </span>
    <span class="social-sq" style="background:#e4405f;margin-left:12px" role="img" aria-label="Pixtale"></span>
    <span class="social-sq" style="background:#e5161a" role="img" aria-label="Vidora"></span>
    <span class="social-sq" style="background:#1b6fe0" role="img" aria-label="Frendly"></span>
  </div>
  <nav class="abs nav">
    <span>Glass Tile ⌄</span><span>Porcelain Tile ⌄</span><span>Ceramic Tile ⌄</span><span>Metal &amp; Stone ⌄</span><span>Our Resources ⌄</span><span>Contact Us</span><span>Sign In or Register</span>
  </nav>
</header>

<section class="hero">
  <h1 class="abs serif hero-title" style="font-weight:500">Italian Porcelain<br>Masterpieces</h1>
  <p class="abs hero-text">Known For Its Striking Sheen And Vivid, Long-Lasting Colors, Our Glass Tile Brings A Luxurious Dimension To Modern And Classic Decors Alike.</p>
  <a class="abs btn" style="left:117px;top:514px;width:143px;height:47px">SHOP NOW ⟶</a>
  <div class="abs fill" style="left:611px;top:210px;width:471px;height:418px;background:linear-gradient(135deg,#3a3a3c 0%,#d9d9db 35%,#eeeeee 60%,#8c8a87 100%)" role="img" aria-label="Modern dining room with dark shelving and white cabinets"></div>
</section>

<section>
  <h2 class="abs serif section-title" style="top:672px;font-weight:500">Start Your Journey</h2>
  <div class="abs journey-card" style="left:117px;background:linear-gradient(#cfcfcf,#f1f1f1 40%,#b9b9b9)" role="img" aria-label="Bathroom with terrazzo glass tile"></div>
  <div class="abs journey-card" style="left:364px;background:linear-gradient(#d8d5d1,#eeeeec 60%,#b7b4b0)" role="img" aria-label="Bathroom with porcelain tile and freestanding tub"></div>
  <div class="abs journey-card" style="left:611px;background:linear-gradient(#e3e6e6,#1f5b60 45%,#30403f)" role="img" aria-label="Kitchen with teal ceramic backsplash"></div>
  <div class="abs journey-card" style="left:857px;background:linear-gradient(#f3f3f2,#d9dcd6 60%,#9fb3a8)" role="img" aria-label="Bathroom with patterned stone floor and clawfoot tub"></div>
  <div class="abs journey-label" style="left:117px">GLASS TILE</div>
  <div class="abs journey-label" style="left:364px">PORCELAIN TILE</div>
  <div class="abs journey-label" style="left:611px">CERAMIC TILE</div>
  <div class="abs journey-label" style="left:857px">METAL &amp; STONE</div>
</section>

<section class="abs dark">
  <h2 class="abs serif section-title" style="top:52px;font-weight:500">Explore The Collections</h2>
  <div class="abs coll-img" style="left:118px;background:linear-gradient(#8f9194,#c8cbcf 45%,#9c9fa3)" role="img" aria-label="Kitchen with striped glass tile backsplash"></div>
  <div class="abs coll-img" style="left:447px;background:linear-gradient(90deg,#d8cdbd,#8f8f8f 50%,#a7a8a7)" role="img" aria-label="Bathroom with gray ceramic wall tile"></div>
  <div class="abs coll-img" style="left:775px;background:linear-gradient(#c9c6c1,#d8d6d2 50%,#b5b3ae)" role="img" aria-label="Living room with porcelain floor tile"></div>
  <div class="abs coll-title" style="left:118px">GLASS COLLECTION</div>
  <div class="abs coll-title" style="left:447px">CERAMIC COLLECTION</div>
  <div class="abs coll-title" style="left:775px">PORCELAIN COLLECTION</div>
  <p class="abs coll-text" style="left:118px">Known For Its Striking Sheen And Vivid, Long-Lasting Colors, Our Glass Tile Brings A Luxurious Dimension To Modern And Classic Decors Alike.</p>
  <p class="abs coll-text" style="left:447px">Crafted For Both Strength And Elegance, Our Ceramic Tile Transforms Any Space With Its Rich Textures And Array Of Hues, Adding A Touch Of Timeless Beauty To Your Decor.</p>
  <p class="abs coll-text" style="left:775px">Renowned For Its Robustness And Refined Finish, Our Porcelain Tile Is Perfect For Both Indoor And Outdoor Settings, Offering A Blend Of Longevity And Luxury In An Array Of Designs.</p>
  <a class="abs btn solid" style="left:200px;top:551px;width:143px;height:46px">SHOP NOW ⟶</a>
  <a class="abs btn dark-outline" style="left:528px;top:551px;width:143px;height:46px">SHOP NOW ⟶</a>
  <a class="abs btn dark-outline" style="left:856px;top:551px;width:143px;height:46px">SHOP NOW ⟶</a>
</section>

<section>
  <h2 class="abs serif section-title" style="top:1754px;font-weight:500">Find Your Color</h2>
  <div class="abs swatch" style="left:121px;background:radial-gradient(circle,#ffffff 30%,#f0f0f0 60%)" role="img" aria-label="White mosaic tile sample"></div>
  <div class="abs swatch" style="left:361px;background:radial-gradient(circle,#a9c6ee 30%,#dbe6fb 60%)" role="img" aria-label="Blue glass subway tile sample"></div>
  <div class="abs swatch" style="left:601px;background:radial-gradient(circle,#7d7673 30%,#d6d6d6 60%)" role="img" aria-label="Gray stone-look tile sample"></div>
  <div class="abs swatch" style="left:841px;background:radial-gradient(circle,#0c4a3f 35%,#c0f6df 60%)" role="img" aria-label="Green glossy tile sample"></div>
  <div class="abs color-label" style="left:121px">WHITES</div>
  <div class="abs color-label" style="left:361px">BLUES</div>
  <div class="abs color-label" style="left:601px">GRAYS</div>
  <div class="abs color-label" style="left:841px">GREENS</div>
  <div class="abs dots" style="left:121px"><span style="background:#fff;border:1px solid #bbb"></span><span style="background:#f4f4f4;border:1px solid #bbb"></span><span style="background:#e4e4e4;border:1px solid #bbb"></span><span style="background:#cfcfcf;border:1px solid #bbb"></span></div>
  <div class="abs dots" style="left:361px"><span style="background:#a6c1f3"></span><span style="background:#6d9be0"></span><span style="background:#2f8ce0"></span><span style="background:#1f4fd8"></span></div>
  <div class="abs dots" style="left:601px"><span style="background:#d8d8d8"></span><span style="background:#aaa5a6"></span><span style="background:#807778"></span><span style="background:#5d5253"></span></div>
  <div class="abs dots" style="left:841px"><span style="background:#9ee8c6"></span><span style="background:#6ed9a8"></span><span style="background:#2fcf86"></span><span style="background:#1fb36b"></span></div>
  <a class="abs btn" style="left:528px;top:2159px;width:143px;height:46px;font-size:11.5px">VIEW ALL COLORS ⟶</a>
  <div class="abs" style="left:117px;top:2263px;width:965px;border-top:1px solid var(--line)"></div>
</section>

<section>
  <h2 class="abs serif section-title" style="top:2306px;font-weight:500">#Vantrisco</h2>
  <div class="abs gallery" style="left:3px;background:linear-gradient(90deg,#3b3b3d,#bfc0bf 55%,#efefee)" role="img" aria-label="Dark bathroom with freestanding tub"></div>
  <div class="abs gallery" style="left:302px;background:linear-gradient(90deg,#151517,#3a3a3c 60%,#e9e9ea)" role="img" aria-label="Black subway tile wall with gold accents"></div>
  <div class="abs gallery" style="left:601px;background:linear-gradient(#e9e7e3,#cfcac3 70%,#b9b4ad)" role="img" aria-label="Bright bathroom with tub by a window"></div>
  <div class="abs gallery" style="left:899px;width:298px;background:linear-gradient(90deg,#9aa5b0,#c8ced3 50%,#e9e8e5)" role="img" aria-label="Blue-gray tile wall with lounge chair"></div>
  <span class="abs cart-pin" style="left:233px;top:2625px"><svg width="18" height="18" viewBox="0 0 18 18" fill="none" stroke="#aaa" stroke-width="1.6"><path d="M1 2h3l2 9h9l2-6H5"/><circle cx="7" cy="15" r="1.3"/><circle cx="14" cy="15" r="1.3"/></svg></span>
  <span class="abs cart-pin on" style="left:533px;top:2625px"><svg width="18" height="18" viewBox="0 0 18 18" fill="none" stroke="#fff" stroke-width="1.6"><path d="M1 2h3l2 9h9l2-6H5"/><circle cx="7" cy="15" r="1.3"/><circle cx="14" cy="15" r="1.3"/></svg></span>
  <span class="abs cart-pin" style="left:831px;top:2625px"><svg width="18" height="18" viewBox="0 0 18 18" fill="none" stroke="#aaa" stroke-width="1.6"><path d="M1 2h3l2 9h9l2-6H5"/><circle cx="7" cy="15" r="1.3"/><circle cx="14" cy="15" r="1.3"/></svg></span>
  <span class="abs cart-pin" style="left:1131px;top:2618px"><svg width="18" height="18" viewBox="0 0 18 18" fill="none" stroke="#aaa" stroke-width="1.6"><path d="M1 2h3l2 9h9l2-6H5"/><circle cx="7" cy="15" r="1.3"/><circle cx="14" cy="15" r="1.3"/></svg></span>
</section>

<section>
  <h2 class="abs serif section-title" style="top:2734px;font-weight:500">Our Happy Clients Says</h2>
  <p class="abs" style="left:320px;top:2808px;width:560px;text-align:center;font-size:14px;line-height:24px;color:var(--muted)">Known For Its Striking Sheen And Vivid, Long-Lasting Colors, Our Glass Tile Brings A Luxurious Dimension To Modern And Classic Decors Alike.</p>
  <svg class="abs" style="left:70px;top:3018px" width="28" height="16" viewBox="0 0 28 16" fill="none" stroke="#111" stroke-width="1.8"><path d="M27 8H2M9 1L2 8l7 7"/></svg>
  <svg class="abs" style="left:1102px;top:3018px" width="28" height="16" viewBox="0 0 28 16" fill="none" stroke="#111" stroke-width="1.8"><path d="M1 8h25M19 1l7 7-7 7"/></svg>
  <article class="abs review" style="left:117px">
    <div class="quote">”</div><div class="stars">★★★★★</div>
    <p>Lorem Ipsum is simply dummy text of the printing and typesetting industry. Lorem Ipsum has been the industry's standard dummy text ever since the 1500s</p>
    <div class="name">Marcel Doria</div><div class="role">A Happy Cutomers</div>
  </article>
  <article class="abs review focus" style="left:446px">
    <div class="quote badge">”</div><div class="stars">★★★★★</div>
    <p>Lorem Ipsum is simply dummy text of the printing and typesetting industry. Lorem Ipsum has been the industry's standard dummy text ever since the 1500s</p>
    <div class="name">Lena Fosberg</div><div class="role">A Happy Cutomers</div>
  </article>
  <article class="abs review" style="left:775px">
    <div class="quote">”</div><div class="stars">★★★★★</div>
    <p>Lorem Ipsum is simply dummy text of the printing and typesetting industry. Lorem Ipsum has been the industry's standard dummy text ever since the 1500s</p>
    <div class="name">Teo Marchetti</div><div class="role">A Happy Cutomers</div>
  </article>
  <div class="abs" style="left:0;top:3211px;width:1200px;text-align:center;font-size:15px;color:var(--star);letter-spacing:4px">★★★★★ <span style="font-family:var(--serif);font-size:11px;color:var(--ink);letter-spacing:0">55988 Reviews</span></div>
</section>

<footer class="abs footer">
  <div class="abs brand light" style="left:117px;top:58px"><span class="mark"></span>Vantrisco</div>
  <div class="abs f-head" style="left:117px;top:140px">Contact Us</div>
  <div class="abs f-contact" style="left:117px;top:168px"><span class="ic"><svg width="14" height="14" viewBox="0 0 14 14" fill="#fff"><path d="M3 1l2 3-1.3 1.3c.8 1.8 2.2 3.2 4 4L9 8l3 2-1 3C5.8 12.5 1.5 8.2 1 2z"/></svg></span>555-014-7720</div>
  <div class="abs f-contact" style="left:117px;top:215px"><span class="ic"><svg width="16" height="12" viewBox="0 0 16 12" fill="none" stroke="#fff" stroke-width="1.4"><rect x="1" y="1" width="14" height="10"/><path d="M1 1l7 6 7-6"/></svg></span>hello@vantrisco.example</div>

  <div class="abs f-head" style="left:420px;top:56px">Client's Experience</div>
  <ul class="abs f-list" style="left:420px;top:86px"><li>Shipping &amp; Returns</li><li>FAQs</li><li>My Account</li><li>Track My Order</li><li>Installation</li></ul>

  <div class="abs f-head" style="left:601px;top:56px">About Vantrisco</div>
  <ul class="abs f-list" style="left:601px;top:86px"><li>About Us</li><li>Inspiration</li><li>Trade</li><li>Inspiration</li><li>Trade Professionals</li><li>Tileist Learning Center</li><li>Sustainability</li></ul>

  <div class="abs f-head" style="left:826px;top:56px">Subscribe Us</div>
  <div class="abs" style="left:826px;top:110px;width:256px;height:46px;border:1px solid #fff;display:flex">
    <span style="flex:1;font-size:12px;padding-left:20px;line-height:44px">Email</span>
    <span style="width:94px;background:#fff;color:var(--ink);font-size:13px;font-weight:500;text-align:center;line-height:44px">SUBSCRIBE</span>
  </div>
  <div class="abs f-head" style="left:826px;top:180px">Find Us On</div>
  <span class="abs social-sq" style="left:826px;top:222px;background:#e4405f" role="img" aria-label="Pixtale"></span>

  <div class="abs" style="left:117px;top:332px;font-size:11.5px">© 2024 Vantrisco. All Rights Reserved</div>
  <div class="abs" style="left:769px;top:324px;display:flex;gap:20px">
    <span class="pay">Cardia</span><span class="pay">Orbipay</span><span class="pay">Amplex</span><span class="pay">Paylo</span><span class="pay">Findcard</span>
  </div>
  <span class="abs" style="left:1115px;top:310px;width:56px;height:56px;border-radius:50%;background:#fff;display:flex;align-items:center;justify-content:center">
    <span style="width:36px;height:36px;border-radius:50%;background:var(--ink);display:flex;align-items:center;justify-content:center;gap:3px">
      <i style="width:4px;height:4px;border-radius:50%;background:#fff"></i><i style="width:4px;height:4px;border-radius:50%;background:#fff"></i><i style="width:4px;height:4px;border-radius:50%;background:#fff"></i>
    </span>
  </span>
</footer>

</body>
</html>
```